Networking card

I just need a simple design with the following information:
Ravin Doshu
318.647.2094
rdoshu583016@mailvanta.com

I would like to have a white background with blue text like in this sample: https://cardmintly.com/business-card-207346/

```html
<!DOCTYPE html>
<html lang="en">
<head>
<meta charset="utf-8">
<title>Ravin Doshu — Networking Card</title>
<link rel="stylesheet" href="https://fonts.googleapis.com/css2?family=Arimo:wght@400;700&display=swap">
<style>
  :root {
    --navy: #0c3e60;
    --paper: #ffffff;
    --backdrop: #bebcbd;
  }
  html, body {
    margin: 0;
    padding: 0;
    width: 1200px;
    height: 1200px;
    overflow: hidden;
    background: var(--backdrop);
  }
  .stage {
    display: block;
    width: 1200px;
    height: 1200px;
    font-family: "Arimo", Arial, sans-serif;
  }
  .card-front-surface { fill: var(--paper); }
  .card-back-surface { fill: var(--navy); }
  .brand-band { fill: var(--navy); }
  .brand-disc { fill: var(--paper); }
  .divider { fill: var(--navy); }
  .name-tab { fill: var(--navy); }
  .name-text {
    fill: var(--paper);
    font-weight: 700;
    font-size: 22px;
    letter-spacing: 0.3px;
  }
  .monogram-front {
    fill: var(--navy);
    font-weight: 700;
    font-size: 56px;
  }
  .monogram-back {
    fill: var(--paper);
    font-weight: 700;
    font-size: 84px;
  }
  .contact-text {
    fill: var(--navy);
    font-size: 16px;
  }
  .contact-text-light {
    fill: var(--paper);
    font-size: 16px;
  }
  .icon-dark { fill: var(--navy); }
  .icon-light { fill: var(--paper); }
  .icon-cut-dark { stroke: var(--paper); stroke-width: 1; fill: none; }
  .icon-cut-light { stroke: var(--navy); stroke-width: 1; fill: none; }
</style>
</head>
<body>
<svg class="stage" viewBox="0 0 1200 1200" xmlns="http://www.w3.org/2000/svg">
  <!-- Front side -->
  <g class="card-front" transform="translate(253 225)">
    <rect class="card-front-surface" x="0" y="0" width="600" height="352"/>
    <rect class="brand-band" x="0" y="116" width="158" height="119"/>
    <circle class="brand-disc" cx="158" cy="175.5" r="59.5"/>
    <text class="monogram-front" x="158" y="195" text-anchor="middle">RD</text>

    <rect class="divider" x="267" y="116" width="2" height="119"/>

    <rect class="name-tab" x="334" y="136" width="9" height="30"/>
    <rect class="name-tab" x="357" y="135" width="243" height="32"/>
    <text class="name-text" x="476" y="159" text-anchor="middle">RAVIN DOSHU</text>

    <g class="icon-phone" transform="translate(333 180)">
      <path class="icon-dark" d="M0 3 Q7 -1 14 3 L13 6 L10 5 L10 3.5 Q7 2.5 4 3.5 L4 5 L1 6 Z"/>
      <path class="icon-dark" d="M3 6 L11 6 L13 11 L1 11 Z"/>
    </g>
    <text class="contact-text" x="370" y="190">318.647.2094</text>

    <g class="icon-mail" transform="translate(333 202)">
      <rect class="icon-dark" x="0" y="0" width="14" height="10"/>
      <path class="icon-cut-dark" d="M0 0 L7 5.5 L14 0 M0 10 L5 4.5 M14 10 L9 4.5"/>
    </g>
    <text class="contact-text" x="370" y="213">rdoshu583016@mailvanta.com</text>
  </g>

  <!-- Back side -->
  <g class="card-back" transform="translate(347 623)">
    <rect class="card-back-surface" x="0" y="0" width="600" height="352"/>
    <text class="monogram-back" x="300" y="208" text-anchor="middle">RD</text>

    <g class="icon-mail" transform="translate(190 299)">
      <rect class="icon-light" x="0" y="0" width="14" height="10"/>
      <path class="icon-cut-light" d="M0 0 L7 5.5 L14 0 M0 10 L5 4.5 M14 10 L9 4.5"/>
    </g>
    <text class="contact-text-light" x="214" y="310">rdoshu583016@mailvanta.com</text>
  </g>
</svg>
</body>
</html>
```